VORL Pty Ltd Business Card

Looking for a simple yet eye-catching double-sided business card design using my company logo on one side and contact details on the other.

Target Market(s)

Government

Industry/Entity Type

Communication Systems Engineering

Contact Information for Business Card

VORL Pty Ltd

Requirements
Nice to have
• Would be great to have a QR code so details can be scanned into contacts

```html
<!DOCTYPE html>
<html lang="en">
<head>
<meta charset="utf-8">
<title>VORL Pty Ltd Business Card</title>
<link href="https://fonts.googleapis.com/css2?family=Josefin+Sans:wght@400;600&family=Montserrat:wght@600;700&display=swap" rel="stylesheet">
<style>
  :root {
    --backdrop: #79b7f1;
    --card-light: #ffffff;
    --card-dark: #2b2b2b;
    --ink: #2f3438;
    --ink-soft: #3a3f44;
    --paper: #ffffff;
    --shadow: rgba(20, 50, 90, 0.45);
  }
  * { margin: 0; padding: 0; box-sizing: border-box; }
  html, body {
    width: 1200px;
    height: 1200px;
    overflow: hidden;
    background: var(--backdrop);
  }
  .canvas {
    position: relative;
    width: 1200px;
    height: 1200px;
  }
  .card {
    position: absolute;
    left: 174px;
    width: 852px;
    height: 510px;
    box-shadow: 0 10px 40px var(--shadow);
  }
  .card--front { top: 64px; background: var(--card-light); }
  .card--back { top: 625px; background: var(--card-dark); }

  /* Front */
  .divider {
    position: absolute;
    left: 408px;
    width: 36px;
    background: var(--card-dark);
  }
  .divider--top { top: 0; height: 180px; }
  .divider--bottom { top: 438px; height: 72px; }
  .divider__icon {
    position: absolute;
    left: 8px;
    top: 98px;
    width: 20px;
    height: 22px;
  }
  .brand {
    position: absolute;
    font-family: "Montserrat", sans-serif;
    font-weight: 700;
    letter-spacing: 2px;
    line-height: 1;
  }
  .brand--front {
    left: 60px;
    width: 270px;
    top: 290px;
    text-align: center;
    font-size: 70px;
    color: var(--ink-soft);
  }
  .identity {
    position: absolute;
    left: 474px;
    top: 98px;
    color: var(--ink);
  }
  .identity__name {
    font-family: "Montserrat", sans-serif;
    font-weight: 600;
    font-size: 41px;
    letter-spacing: 3px;
    line-height: 1;
  }
  .identity__role {
    margin-top: 10px;
    font-family: "Josefin Sans", sans-serif;
    font-weight: 400;
    font-size: 27px;
    letter-spacing: 2px;
    line-height: 1;
  }
  .contacts {
    position: absolute;
    left: 408px;
    top: 238px;
    list-style: none;
  }
  .contact {
    display: flex;
    align-items: center;
    height: 36px;
    margin-bottom: 16px;
    font-family: "Josefin Sans", sans-serif;
    color: var(--ink);
  }
  .contact__icon {
    width: 36px;
    height: 36px;
    border-radius: 5px;
    background: var(--card-dark);
    display: flex;
    align-items: center;
    justify-content: center;
    flex-shrink: 0;
  }
  .contact__text {
    margin-left: 24px;
    font-size: 25px;
    line-height: 1.1;
    padding-top: 4px;
  }
  .contact__text--address {
    font-size: 19px;
    line-height: 1.25;
    margin-top: 12px;
  }

  /* Back */
  .back-mark {
    position: absolute;
    left: 160px;
    top: 155px;
    display: flex;
    align-items: center;
    gap: 60px;
  }
  .back-mark__dot {
    width: 140px;
    height: 140px;
    border-radius: 50%;
    border: 4px solid var(--paper);
  }
  .brand--back {
    position: static;
    font-size: 100px;
    color: var(--paper);
    letter-spacing: 4px;
  }
</style>
</head>
<body>
<main class="canvas">

  <section class="card card--front" aria-label="Business card front">
    <div class="brand brand--front">VORL</div>

    <div class="divider divider--top">
      <svg class="divider__icon" viewBox="0 0 20 22" aria-hidden="true">
        <circle cx="10" cy="6" r="5.5" fill="#fff"/>
        <path d="M0 22 C0 14 20 14 20 22 Z" fill="#fff"/>
      </svg>
    </div>
    <div class="divider divider--bottom"></div>

    <div class="identity">
      <h1 class="identity__name">DANIEL REEVE</h1>
      <p class="identity__role">CEO DIRECTOR</p>
    </div>

    <ul class="contacts">
      <li class="contact">
        <span class="contact__icon">
          <svg width="20" height="20" viewBox="0 0 24 24" aria-hidden="true">
            <path fill="#fff" d="M6.6 10.8a15.1 15.1 0 0 0 6.6 6.6l2.2-2.2a1 1 0 0 1 1-.25 11.4 11.4 0 0 0 3.6.57 1 1 0 0 1 1 1V20a1 1 0 0 1-1 1A17 17 0 0 1 3 4a1 1 0 0 1 1-1h3.5a1 1 0 0 1 1 1c0 1.25.2 2.45.57 3.6a1 1 0 0 1-.25 1z"/>
          </svg>
        </span>
        <span class="contact__text">+000 123-456-789</span>
      </li>
      <li class="contact">
        <span class="contact__icon">
          <svg width="22" height="16" viewBox="0 0 22 16" aria-hidden="true">
            <rect x="1" y="1" width="20" height="14" fill="none" stroke="#fff" stroke-width="2"/>
            <path d="M1 1 L11 9 L21 1" fill="none" stroke="#fff" stroke-width="2"/>
          </svg>
        </span>
        <span class="contact__text">admin@vorl.com.au</span>
      </li>
      <li class="contact">
        <span class="contact__icon">
          <svg width="22" height="20" viewBox="0 0 22 20" aria-hidden="true">
            <path fill="#fff" d="M11 1 L1 10 H4 V19 H9 V13 H13 V19 H18 V10 H21 Z"/>
          </svg>
        </span>
        <span class="contact__text contact__text--address">14-16 Harlow Lane Redfield<br>NSW 2150 Australia</span>
      </li>
    </ul>
  </section>

  <section class="card card--back" aria-label="Business card back">
    <div class="back-mark">
      <span class="back-mark__dot" aria-hidden="true"></span>
      <div class="brand brand--back">VORL</div>
    </div>
  </section>

</main>
</body>
</html>
```